Badge concepts rewarding users that take action on climate change

Start simple! Show your style, concepts. We're excited to collaborate on this project!

We have built a platform to help tackle climate change via education, reductions and carbon offsetting. To reward user engagement and user milestones, we want to offer about 10 badges. Some example badges are:

- Carbon aware: calculated their carbon footprint - Themes: Awareness, clarity, calculator
- Climate action award: Have offset some of their emissions - Themes: Taking action, energy, running, movement
- Climate hero, multi-tier badge: 3 months carbon neutral, 6 months carbon neutral, 12 months carbon neutral etc. - Themes: feel good, happy, green, planet, neutrality, balance
- Climate Friendly Traveller: Have offset some/all of their travel-related emissions - Themes: car, driving, flight, green
- Climate Friendly Eater: Have offset some/all of their eating & Diet-related emissions - Themes: eating, food, green
- Climate Friendly Living: Have offset some/all of their living and consumption-related emissions - Themes: purchasing, housing, e-commerce, green
- Climate Friendly Energy: Have offset some/all of their energy-related emissions - Themes: power, natural gas, green
- Climate action movement: is part of a group of individuals taking action on climate change. - Themes: Group, people, friends, planet, green, nature
- Climate friendly team: is part of a group of company taking action on climate change. - Themes: Staff, team, people, planet, green, nature
- Climate Friendly Merchant: Is a e-commerce store-owner who has installed climate friendly cart - Themes: E-commerce, shopping, online shopping cart.

The badges must work in 3 sizes - with varying levels of detail: Large, when a user clicks the badge (about 400px wide), Medium, on the users dashboard (about 80px) and Small, on the team page (about 40px).

At this point - please feel free to submit a single badge, conceptual, showing your style and unique thinking around the opportunity. We will happily reward the winning design with additional work.

Font styles to use
Sans Serif

Requirements
Must have
• Use multiple shades/colours
Nice to have
• Explore using Imagery/photography
Should not have
• Cheap generic icons

```html
<!DOCTYPE html>
<html lang="en">
<head>
<meta charset="utf-8">
<title>Verda Dashboard – Carbon Aware Badge</title>
<link href="https://fonts.googleapis.com/css2?family=Roboto:wght@300;400;500&family=Montserrat:wght@500;700&display=swap" rel="stylesheet">
<style>
  :root{
    --green-deep:#047a3f;
    --green-side:#4c8e47;
    --green-head:#62ab57;
    --green-dark:#2a6b33;
    --tan:#d49a5e;
    --brown-bar:#b3874f;
    --brown-text:#b07f45;
    --brown-dark:#6e4a23;
    --navy:#231b5c;
    --canvas:#f2f2f2;
    --card:#ffffff;
    --text-green:#4c8e47;
    --muted:#8a8a8a;
    --overlay:rgba(96,96,100,.8);
    --map:#e6e9e6;
    --red:#e8453c;
  }
  *{box-sizing:border-box;margin:0;padding:0}
  html,body{width:1200px;height:812px;overflow:hidden;background:#fff}
  body{font-family:"Roboto",Arial,sans-serif;position:relative;color:#333}
  .app{position:absolute;left:18px;top:18px;width:1163px;height:776px;border-radius:31px;overflow:hidden;background:var(--canvas)}
  .sidebar{position:absolute;left:0;top:0;width:244px;height:100%;background:var(--green-side)}
  .brand-bar{position:absolute;left:0;top:0;width:244px;height:60px;background:var(--green-deep)}
  .hamburger{position:absolute;left:28px;top:24px;width:31px;height:16px;display:flex;flex-direction:column;justify-content:space-between}
  .hamburger span{height:2px;background:var(--tan)}
  .brand{position:absolute;left:84px;top:14px;font-size:27px;font-weight:400;color:#fff;letter-spacing:1px}
  .nav{position:absolute;left:0;top:0;list-style:none}
  .nav li{position:absolute;left:40px;height:24px;display:flex;align-items:center;font-size:18px;font-weight:300;color:#fff;white-space:nowrap}
  .nav li svg{width:22px;height:22px;margin-right:13px}
  .nav li.active{color:var(--tan)}
  .count{margin-left:16px;background:var(--red);color:#fff;font-size:13px;width:23px;height:20px;display:flex;align-items:center;justify-content:center}
  .topbar{position:absolute;left:244px;top:0;right:0;height:60px;background:var(--green-head)}
  .search{position:absolute;left:46px;top:17px;width:234px;height:32px;background:#fff;border-radius:16px;font-size:14px;font-weight:300;color:#888;padding:7px 20px;display:flex;justify-content:space-between;align-items:center}
  .greeting{position:absolute;right:102px;top:18px;font-size:21px;font-weight:300;color:#fff}
  .avatar{position:absolute;right:52px;top:10px;width:42px;height:42px;border-radius:50%;background:#fff;overflow:hidden}
  .badge-strip{position:absolute;left:952px;top:60px;width:211px;height:31px}
  h1.page-title{position:absolute;left:279px;top:104px;font-size:31px;font-weight:300;color:var(--navy)}
  .card{position:absolute;background:var(--card);border-radius:12px}
  .card-title{position:absolute;font-size:14px;font-weight:300;color:var(--text-green)}
  .card svg{position:absolute;left:0;top:0}
  .milestone{position:absolute;top:46px;width:110px;margin-left:-55px;display:flex;flex-direction:column;align-items:center;text-align:center}
  .milestone .label{font-size:10.5px;font-weight:300;color:var(--muted);height:14px}
  .milestone .icon{height:34px;margin-top:4px;display:flex;align-items:center;justify-content:center}
  .milestone .icon svg{position:static}
  .milestone .value{font-family:"Montserrat",sans-serif;font-size:16px;font-weight:500;color:var(--brown-text);margin-top:6px;line-height:20px}
  .milestone .note{font-size:6.5px;color:#666;margin-top:3px}
  .your-badges .card-title{left:0;right:0;text-align:center;top:16px;line-height:17px;color:var(--text-green)}
  .mini-badge{position:absolute;left:35px;width:48px;height:48px;border-radius:50%}
  .mini-label{position:absolute;left:0;right:0;text-align:center;font-size:9.5px;font-weight:300;color:var(--text-green)}
  .pager{position:absolute;left:0;right:0;top:326px;text-align:center;font-size:11px;color:#555;word-spacing:14px}
  .update-title{position:absolute;left:19px;top:12px;font-size:10px;font-weight:300;color:var(--muted)}
  .update-date{position:absolute;right:21px;top:12px;font-size:8.5px;font-weight:500;color:var(--text-green)}
  .update-body{position:absolute;left:19px;top:31px;width:196px;font-size:6.6px;line-height:8.2px;color:#333}
  .legend{position:absolute;font-size:11px;font-weight:300;color:var(--muted)}
  .row-pct{position:absolute;left:194px;font-size:7.5px;color:#999}
  .overlay-art{position:absolute;left:0;top:0;width:1200px;height:812px}
</style>
</head>
<body>
<div class="app">
  <aside class="sidebar">
    <div class="brand-bar">
      <div class="hamburger"><span></span><span></span><span></span></div>
      <div class="brand">Verda</div>
    </div>
    <ul class="nav">
      <li class="active" style="top:157px"><svg viewBox="0 0 22 22"><path d="M11 1 L21 10 H18 V21 H13 V15 H9 V21 H4 V10 H1Z" fill="#d49a5e"/></svg>Dashboard</li>
      <li style="top:217px"><svg viewBox="0 0 22 22"><rect x="1" y="5" width="20" height="13" fill="#7fc06f"/><path d="M1 5 L11 13 L21 5 M1 18 L8 11 M21 18 L14 11" stroke="#4c8e47" stroke-width="1.2" fill="none"/></svg>Messages<span class="count">3</span></li>
      <li style="top:266px"><svg viewBox="0 0 22 22"><circle cx="11" cy="6" r="4.5" fill="#7fc06f"/><path d="M4 21 V15 Q4 11 11 11 Q18 11 18 15 V21Z" fill="#7fc06f"/></svg>Account</li>
      <li style="top:314px"><svg viewBox="0 0 22 22"><path d="M10 3 A9 9 0 1 0 19 12 H10Z" fill="#7fc06f"/><path d="M12 1 A9 9 0 0 1 21 10 H12Z" fill="#7fc06f"/></svg>Games</li>
      <li style="top:363px"><svg viewBox="0 0 22 22"><rect x="1" y="3" width="20" height="13" rx="1.5" fill="#7fc06f"/><path d="M11 16 V20 M8 21 L11 18 L14 21" stroke="#7fc06f" stroke-width="1.2" fill="none"/></svg>Lessons</li>
      <li style="top:412px"><svg viewBox="0 0 22 22"><path d="M11 1 L21 20 H1Z" fill="#7fc06f"/><rect x="10" y="7" width="2" height="7" fill="#4c8e47"/><rect x="10" y="16" width="2" height="2" fill="#4c8e47"/></svg>Reports</li>
    </ul>
  </aside>

  <header class="topbar">
    <div class="search">Search
      <svg width="15" height="15" viewBox="0 0 15 15"><circle cx="6" cy="6" r="4.5" stroke="#555" stroke-width="1.6" fill="none"/><path d="M9.5 9.5 L14 14" stroke="#555" stroke-width="1.8"/></svg>
    </div>
    <div class="greeting">Hi, Maren Oakley</div>
    <div class="avatar"><svg width="42" height="42" viewBox="0 0 42 42"><circle cx="21" cy="17" r="7" fill="#ddd"/><path d="M8 40 Q8 26 21 26 Q34 26 34 40Z" fill="#ddd"/></svg></div>
  </header>

  <svg class="badge-strip" viewBox="0 0 211 31">
    <path d="M0 0 H211 V26 Q211 31 206 31 H12Z" fill="#2b2b2b"/>
    <circle cx="44" cy="15" r="12" fill="#e8a657"/><circle cx="44" cy="15" r="7" fill="none" stroke="#b0702e" stroke-width="1"/>
    <circle cx="83" cy="15" r="12" fill="#dcdcdc"/><circle cx="83" cy="15" r="7" fill="none" stroke="#555" stroke-width="1"/>
    <circle cx="122" cy="15" r="12" fill="#8fcf7f"/><circle cx="122" cy="15" r="7" fill="none" stroke="#2a6b33" stroke-width="1"/>
    <circle cx="162" cy="15" r="12" fill="#c9a27a"/><circle cx="162" cy="15" r="7" fill="none" stroke="#6e4a23" stroke-width="1"/>
  </svg>

  <h1 class="page-title">Overview</h1>

  <section class="card average-charts" style="left:276px;top:165px;width:477px;height:239px">
    <div class="card-title" style="left:27px;top:12px">Average Charts</div>
    <svg width="477" height="239" viewBox="0 0 477 239" font-family="Roboto, sans-serif" font-size="7" fill="#777">
      <g stroke="#d8d8d8" stroke-width="1">
        <line x1="57" y1="69" x2="448" y2="69"/><line x1="57" y1="96" x2="448" y2="96"/>
        <line x1="57" y1="123" x2="448" y2="123"/><line x1="57" y1="150" x2="448" y2="150"/>
        <line x1="57" y1="177" x2="448" y2="177"/>
      </g>
      <text x="30" y="72">3000</text><text x="30" y="99">2500</text><text x="30" y="126">2000</text><text x="30" y="153">1500</text><text x="30" y="180">1000</text>
      <g fill="#62ab57">
        <rect x="57" y="136.5" width="12" height="40.5"/><rect x="109" y="133.8" width="12" height="43.2"/>
        <rect x="161" y="104.1" width="12" height="72.9"/><rect x="213" y="80.9" width="12" height="96.1"/>
        <rect x="264" y="128.4" width="12" height="48.6"/><rect x="312" y="85.2" width="12" height="91.8"/>
        <rect x="368" y="71.7" width="12" height="105.3"/><rect x="420" y="109.5" width="12" height="67.5"/>
      </g>
      <g fill="#b3874f">
        <rect x="73" y="112.2" width="12" height="64.8"/><rect x="125" y="114.9" width="12" height="62.1"/>
        <rect x="177" y="90.6" width="12" height="86.4"/><rect x="229" y="71.7" width="12" height="105.3"/>
        <rect x="280" y="114.9" width="12" height="62.1"/><rect x="328" y="114.9" width="12" height="62.1"/>
        <rect x="384" y="80.9" width="12" height="96.1"/><rect x="436" y="71.7" width="12" height="105.3"/>
      </g>
      <g stroke="#555"><line x1="70" y1="193" x2="70" y2="196"/><line x1="122" y1="193" x2="122" y2="196"/><line x1="174" y1="193" x2="174" y2="196"/><line x1="226" y1="193" x2="226" y2="196"/><line x1="277" y1="193" x2="277" y2="196"/><line x1="325" y1="193" x2="325" y2="196"/><line x1="381" y1="193" x2="381" y2="196"/><line x1="433" y1="193" x2="433" y2="196"/></g>
      <g text-anchor="middle"><text x="70" y="204">01</text><text x="122" y="204">02</text><text x="174" y="204">03</text><text x="226" y="204">04</text><text x="277" y="204">05</text><text x="325" y="204">06</text><text x="381" y="204">07</text><text x="433" y="204">08</text></g>
    </svg>
  </section>

  <section class="card climate-events" style="left:276px;top:414px;width:477px;height:276px">
    <div class="card-title" style="left:27px;top:17px">Climate Events</div>
    <svg width="477" height="276" viewBox="0 0 477 276">
      <defs><path id="pin" d="M0 0 C-2 -4 -5.5 -6.5 -5.5 -10 A5.5 5.5 0 1 1 5.5 -10 C5.5 -6.5 2 -4 0 0Z"/></defs>
      <rect x="36" y="48" width="413" height="186" rx="40" fill="#e6e9e6" role="img" aria-label="World map showing climate event locations"/>
      <g fill="#62ab57">
        <use href="#pin" x="104" y="78"/><use href="#pin" x="318" y="64"/><use href="#pin" x="93" y="133"/><use href="#pin" x="241" y="147"/>
      </g>
      <use href="#pin" x="393" y="107" fill="#2a6b33"/>
      <g fill="#b3874f">
        <use href="#pin" x="65" y="68"/><use href="#pin" x="234" y="78"/><use href="#pin" x="325" y="105"/><use href="#pin" x="149" y="185"/><use href="#pin" x="402" y="200"/>
      </g>
      <use href="#pin" x="250" y="262" fill="#62ab57"/>
      <use href="#pin" x="357" y="262" fill="#b3874f"/>
    </svg>
    <div class="legend" style="left:265px;top:244px">Your Text 01</div>
    <div class="legend" style="left:371px;top:244px">Your Text 02</div>
  </section>

  <section class="card milestones" style="left:764px;top:165px;width:362px;height:158px">
    <div class="card-title" style="left:26px;top:12px">Platform Milestones</div>
    <div class="milestone" style="left:76px">
      <div class="label">Donations</div>
      <div class="icon"><svg width="24" height="34" viewBox="0 0 24 34"><text x="12" y="30" text-anchor="middle" font-family="Montserrat, sans-serif" font-weight="700" font-size="36" fill="#4c9a3f">$</text></svg></div>
      <div class="value">$ 3,124</div><div class="note">*lorem ipsum dolor</div>
    </div>
    <div class="milestone" style="left:182px">
      <div class="label">Lessons Completed</div>
      <div class="icon"><svg width="22" height="30" viewBox="0 0 22 30"><path d="M7 0 H15 V16 H22 L11 29 L0 16 H7Z" fill="#4c9a3f"/></svg></div>
      <div class="value">1,340,210</div><div class="note">*lorem ipsum dolor</div>
    </div>
    <div class="milestone" style="left:289px">
      <div class="label">Badges</div>
      <div class="icon"><svg width="30" height="30" viewBox="0 0 30 30"><path d="M15 1 L19 11 L29 11.5 L21 18 L24 28 L15 22.5 L6 28 L9 18 L1 11.5 L11 11Z" fill="#4c9a3f"/></svg></div>
      <div class="value">135,020</div><div class="note">*lorem ipsum dolor</div>
    </div>
  </section>

  <section class="card progress" style="left:764px;top:333px;width:233px;height:263px">
    <svg width="233" height="263" viewBox="0 0 233 263">
      <rect x="167" y="72" width="19" height="5" fill="#2a6b33"/>
      <rect x="142" y="182" width="25" height="5" fill="#6e4a23"/>
      <rect x="116" y="204" width="14" height="5" fill="#2a6b33"/>
      <rect x="86" y="226" width="66" height="5" fill="#6e4a23"/>
    </svg>
    <div class="row-pct" style="top:70px">98%</div><div class="row-pct" style="top:92px">50%</div>
    <div class="row-pct" style="top:113px">20%</div><div class="row-pct" style="top:135px">45%</div>
    <div class="row-pct" style="top:156px">30%</div><div class="row-pct" style="top:178px">80%</div>
    <div class="row-pct" style="top:199px">39%</div><div class="row-pct" style="top:221px">65%</div>
  </section>

  <section class="card recent-update" style="left:764px;top:608px;width:233px;height:83px">
    <div class="update-title">Recent Update</div>
    <div class="update-date">01/12/2020</div>
    <p class="update-body">Lorem ipsum dolor sit amet, consectetuer adipiscing elit, sed diam nonummy nibh euismod tincidunt ut laoreet dolore magna aliquam erat volutpat. Ut wisi enim ad minim veniam, quis nostrud exerci tation ullamcorper suscipit lobortis.</p>
  </section>

  <section class="card your-badges" style="left:1008px;top:333px;width:118px;height:358px">
    <div class="card-title">Your<br>Badges</div>
    <div class="mini-badge" role="img" aria-label="Carbon Aware badge artwork" style="top:73px;background:radial-gradient(circle at 60% 60%,#8fcf7f 0 40%,#f4f4f4 41%);border:2px solid #d49a5e"></div>
    <div class="mini-label" style="top:126px">Carbon Aware</div>
    <div class="mini-badge" role="img" aria-label="Lorem Ipsum badge artwork" style="top:154px;background:radial-gradient(circle at 45% 60%,#cfcfcf 0 40%,#f4f4f4 41%);border:2px solid #777"></div>
    <div class="mini-label" style="top:207px">Lorem Ipsum</div>
    <div class="mini-badge" role="img" aria-label="Dolor Sit Amet badge artwork" style="top:235px;background:radial-gradient(circle at 60% 60%,#c9a27a 0 40%,#f4f4f4 41%);border:2px solid #62ab57"></div>
    <div class="mini-label" style="top:288px">Dolor Sit Amet</div>
    <div class="pager">‹ 1/3 ›</div>
  </section>
</div>

<svg class="overlay-art" viewBox="0 0 1200 812" font-family="Montserrat, sans-serif">
  <defs>
    <clipPath id="badge-clip"><circle cx="831" cy="439" r="113"/></clipPath>
    <path id="arc-top" d="M737 439 A94 94 0 0 1 925 439"/>
    <path id="arc-bottom" d="M733.7 462 A100 100 0 0 0 928.3 462"/>
  </defs>
  <rect x="671" y="297" width="328" height="290" rx="6" fill="var(--overlay)"/>
  <path d="M999 444 H1053 L999 508Z" fill="var(--overlay)"/>
  <g class="badge-large">
    <circle cx="831" cy="439" r="121" fill="#d49a5e"/>
    <circle cx="831" cy="439" r="113" fill="#f3f4f4"/>
    <g clip-path="url(#badge-clip)">
      <rect x="700" y="464" width="270" height="25" fill="#d49a5e"/>
      <rect x="700" y="489" width="270" height="14" fill="#9a6a3a"/>
    </g>
    <path d="M731.4 447.7 A100 100 0 0 1 773.6 357.1" stroke="#62ab57" stroke-width="2.6" stroke-linecap="round" stroke-dasharray="0 8" fill="none"/>
    <path d="M888.4 357.1 A100 100 0 0 1 930.6 447.7" stroke="#62ab57" stroke-width="2.6" stroke-linecap="round" stroke-dasharray="0 8" fill="none"/>
    <text font-size="15" font-weight="500" fill="#1f3d22" letter-spacing="1"><textPath href="#arc-top" startOffset="50%" text-anchor="middle">CARBON AWARE</textPath></text>
    <circle cx="829" cy="409" r="46" fill="#62ab57" role="img" aria-label="Illustration of a thinking head with a lightbulb beside a green globe"/>
    <text x="831" y="483" text-anchor="middle" font-size="12.5" font-weight="700" fill="#fff" letter-spacing=".5">MAREN OAKLEY</text>
    <text x="831" y="499" text-anchor="middle" font-size="5.8" font-weight="500" fill="#fff">HAS CALCULATED THEIR CARBON FOOTPRINT</text>
    <text x="831" y="528" text-anchor="middle" font-size="11" font-weight="500" fill="#4c9a3f">VERDA</text>
    <text font-size="7" font-weight="500" fill="#222" letter-spacing=".4"><textPath href="#arc-bottom" startOffset="50%" text-anchor="middle">ISSUED BY GREENSTEP-HUB.ORG</textPath></text>
  </g>
  <g class="close-button">
    <circle cx="990" cy="307" r="19" fill="#d49a5e"/>
    <path d="M983 300 L997 314 M997 300 L983 314" stroke="#fff" stroke-width="1.8"/>
  </g>
</svg>
</body>
</html>
```